Glenmorrow ice cream tub packaging

We need new tub designs for our dairy free ice cream. It is made with avocado and coconut which we would like communicated within the design. We launched last year and have had positive feedback regarding our current packaging but also that it could be a cleaner design with a more sophisticated font as it will be sold in more high end expensive stores. I have attached our current packaging for info (there are 3 flavours - Original Avocado, Raspberry and Basil, Raw Cacao) We would like to keep the avocado print that is currently included on the packaging as we have had a lot of very positive feedback about that. Maybe not as much though as it makes it quite busy and we prefer a clean design.
I've also attached our new logo.
We would like it to mention we are gluten, soya, dairy, egg and nut free. And that it is a 'coconut and avocado ice cream' rather than an 'alternative'.
The nutritional label needs to be in a UK table format (I've attached a blank copy for information). We don't currently have the values for the table as it has been sent off for testing as we have a new recipe. But if you could leave that blank we will fill it in when we have the results.
I've attached the template for the sizes as we have two sizes - 500ml and 100ml. The designs will be the same but just smaller/bigger. It has to be font size 11 for legal purpose.
It has to have the weight (100ml and 500ml) followed by the official e-mark.
The ingredients are the same but take out Locust Bean Gum and replace Vanilla extract with Lime Juice.
The business address is the same but should read 'Glenmorrow LTD'. All other info on the packaging (barcode, text etc) is to remain the same.
I've have also attached 3 pictures of other tub designs that we like for inspiration - our favourite is 'zelt' as we can have half the print half the colour if the flavour (raspberry/pink, cacao/brown, original/green)
Updates
Target Market(s)
High end health food stores
Look and feel

```html
<!DOCTYPE html>
<html lang="en">
<head>
<meta charset="utf-8">
<title>Glenmorrow Ice Cream Tub Wraps</title>
<link rel="stylesheet" href="https://fonts.googleapis.com/css2?family=Questrial&family=Arimo:wght@400;700&display=swap">
<style>
  :root {
    --bg-top: #f3f5ea;
    --bg-bottom: #fbfdf2;
    --label-black: #050505;
    --brand-green: #8cc63f;
    --text-white: #ffffff;
    --text-pink: #f6a9c2;
    --text-dark: #1a1a1a;
    --print-light: #e6f4bb;
    --print-mid: #b9d676;
    --print-deep: #93b84c;
    --original-a: #c4e08f;
    --original-b: #e2f3b7;
    --cacao-a: #5a2216;
    --cacao-b: #d99a74;
    --berry-a: #cf3c63;
    --berry-b: #f79ab6;
  }
  * { box-sizing: border-box; margin: 0; padding: 0; }
  html, body { width: 1200px; height: 600px; overflow: hidden; }
  body {
    background: linear-gradient(180deg, var(--bg-top), var(--bg-bottom));
    display: flex;
    align-items: center;
    justify-content: center;
    gap: 50px;
  }
  .tub-wrap {
    position: relative;
    width: 330px;
    height: 380px;
    overflow: hidden;
  }
  .avocado-print {
    position: absolute;
    inset: 0;
    background: linear-gradient(90deg, var(--print-light) 0%, var(--print-mid) 55%, var(--print-deep) 100%);
  }
  .flavour-colour {
    position: absolute;
    inset: 0;
    clip-path: polygon(0 0, 54% 0, 62% 100%, 0 100%);
  }
  .flavour-original .flavour-colour { background: linear-gradient(90deg, var(--original-a), var(--original-b)); }
  .flavour-cacao .flavour-colour { background: linear-gradient(90deg, var(--cacao-a), var(--cacao-b)); }
  .flavour-berry .flavour-colour { background: linear-gradient(90deg, var(--berry-a), var(--berry-b)); }

  .front-label {
    position: absolute;
    left: 58px;
    top: 62px;
    width: 214px;
    height: 238px;
    background: var(--label-black);
    clip-path: polygon(0 0, 100% 0, 94% 100%, 6% 100%);
    border-radius: 0 0 14px 14px;
    text-align: center;
    padding-top: 22px;
  }
  .brand-name {
    font-family: "Questrial", sans-serif;
    font-size: 15px;
    letter-spacing: 1px;
    color: var(--brand-green);
    display: flex;
    align-items: center;
    justify-content: center;
    gap: 5px;
  }
  .brand-dot {
    width: 9px; height: 9px;
    border-radius: 50%;
    background: var(--brand-green);
  }
  .tagline {
    font-family: "Questrial", sans-serif;
    font-size: 8px;
    color: var(--text-white);
    margin-top: 5px;
  }
  .flavour-title {
    font-family: "Questrial", sans-serif;
    font-weight: 400;
    color: var(--text-white);
    margin-top: 24px;
    line-height: 1.02;
  }
  .flavour-title .lead { display: block; font-size: 21px; }
  .flavour-title .rest { display: block; font-size: 14px; line-height: 1.2; margin-top: 2px; }
  .flavour-original .flavour-title .rest { font-size: 21px; line-height: 1.02; margin-top: 0; }
  .flavour-berry .flavour-title { color: var(--text-pink); }
  .free-from {
    position: absolute;
    left: 0;
    right: 0;
    bottom: 34px;
    font-family: "Arimo", sans-serif;
    font-size: 11px;
    line-height: 1.15;
    color: var(--text-white);
  }
  .volume {
    position: absolute;
    left: 0;
    right: 0;
    top: 316px;
    text-align: center;
    font-family: "Arimo", sans-serif;
    font-weight: 700;
    font-size: 13px;
    color: var(--text-dark);
    padding-left: 20px;
  }
  .e-mark { font-size: 18px; font-weight: 400; vertical-align: -1px; }
</style>
</head>
<body>
  <section class="tub-wrap flavour-original">
    <div class="avocado-print" role="img" aria-label="Repeating pattern of halved avocados on pale green"></div>
    <div class="flavour-colour"></div>
    <div class="front-label">
      <p class="brand-name"><span class="brand-dot"></span>GLENMORROW</p>
      <p class="tagline">Simply Green &amp; Creamy</p>
      <h2 class="flavour-title"><span class="lead">Avocado<br>and</span><span class="rest">Coconut Milk<br>Ice Cream</span></h2>
      <p class="free-from">gluten soya dairy<br>egg and nut free</p>
    </div>
    <p class="volume">500ml <span class="e-mark">℮</span></p>
  </section>

  <section class="tub-wrap flavour-cacao">
    <div class="avocado-print" role="img" aria-label="Repeating pattern of halved avocados on pale green"></div>
    <div class="flavour-colour"></div>
    <div class="front-label">
      <p class="brand-name"><span class="brand-dot"></span>GLENMORROW</p>
      <p class="tagline">Simply Green &amp; Creamy</p>
      <h2 class="flavour-title"><span class="lead">Avocado<br>and</span><span class="rest">Coconut Ice Cream<br>with Raw Cacao</span></h2>
      <p class="free-from">gluten soya dairy<br>egg and nut free</p>
    </div>
    <p class="volume">500ml <span class="e-mark">℮</span></p>
  </section>

  <section class="tub-wrap flavour-berry">
    <div class="avocado-print" role="img" aria-label="Repeating pattern of halved avocados on pale green"></div>
    <div class="flavour-colour"></div>
    <div class="front-label">
      <p class="brand-name"><span class="brand-dot"></span>GLENMORROW</p>
      <p class="tagline">Simply Green &amp; Creamy</p>
      <h2 class="flavour-title"><span class="lead">Avocado<br>and</span><span class="rest">Coconut Ice Cream<br>with Raspberry &amp; Basil</span></h2>
      <p class="free-from">gluten soya dairy<br>egg and nut free</p>
    </div>
    <p class="volume">500ml <span class="e-mark">℮</span></p>
  </section>
</body>
</html>
```